Emerging Australian photographer

I'm based in Cunderdin, a small rural town in the Wheatbelt area of Western Australia. So its a good thing that I love to travel further afield both for pleasure and for work. To me that is one and the same thing in any event!

My desire is to take photos that make the viewers heart skip. I love taking photos of people doing the things they love or being with the people they love. For me, the joy of photography comes with capturing the 'moments between the moments'. I like candid photography best of all - like when the new husband is staring joyfully at his bride and at that minute is unaware of the photographer capturing the moment.

I am available for weddings, engagements, birthdays, special events, newborns, family or individual portraits. By the end of the year I will be accredited with the Southern Guild of Practising Imagemakers.

I need a card that stands out but is elegant and would sit well on the table at a wedding or be given out in the church grounds. Classy and a little bit sassy.

Target Market(s)

Consumers who are seeking photographic services, eg wedding guests who see me at work and make enquiries.

Industry/Entity Type

Church

Contact Information for Business Card

Danielle Whitcombe Photography
Danielle Whitcombe
0438 562 073
www.daniellewhitcombe.com.au
photos@daniellewhitcombe.com.au

Requirements
Must have
• Must fit with the theme in the watermarks, but be crisp and modern.
Nice to have
• However it's not essential to have the pink! Chatterbook and Pipsqueak logos.
Should not have
• Old style fonts like times new roman.

```html
<!DOCTYPE html>
<html lang="en">
<head>
<meta charset="utf-8">
<title>Danielle Whitcombe Photography – Business Card</title>
<link rel="stylesheet" href="https://fonts.googleapis.com/css2?family=Open+Sans:wght@300;400&display=swap">
<style>
  :root {
    --paper-light: #f3f3f2;
    --paper-mid: #e9e9e8;
    --paper-dark: #dcdcdb;
    --ink: #1f1f22;
    --ink-soft: #6d7076;
    --blush: #eba6e0;
    --magenta: #e63ad6;
    --lens-deep: #0b0f22;
    --lens-mid: #1c2547;
    --lens-rim: #3a4670;
  }
  * { margin: 0; padding: 0; box-sizing: border-box; }
  html, body { width: 1200px; height: 741px; overflow: hidden; }
  body { font-family: "Open Sans", sans-serif; color: var(--ink); }
  .card {
    position: relative;
    width: 1200px;
    height: 741px;
    overflow: hidden;
    background: radial-gradient(ellipse at 65% 35%, var(--paper-light) 0%, var(--paper-mid) 60%, var(--paper-dark) 100%);
  }
  .lens-photo { position: absolute; left: 0; top: 0; width: 1200px; height: 741px; }
  .brand {
    position: absolute;
    right: 80px;
    top: 140px;
    display: flex;
    align-items: center;
    gap: 14px;
    font-weight: 300;
    font-size: 30px;
    letter-spacing: 1px;
    color: var(--ink-soft);
  }
  .brand-dot { width: 14px; height: 14px; border-radius: 50%; background: var(--blush); }
  .details {
    position: absolute;
    right: 87px;
    top: 372px;
    text-align: right;
  }
  .name {
    font-weight: 400;
    font-size: 70px;
    line-height: 1;
    letter-spacing: -1px;
    margin-bottom: 24px;
  }
  .name-first { color: var(--blush); }
  .name-last { color: var(--ink); }
  .contact { font-size: 24px; line-height: 39px; color: var(--ink); }
  .social {
    position: absolute;
    right: 86px;
    top: 606px;
    display: flex;
    gap: 26px;
  }
  .social-item {
    display: flex;
    align-items: center;
    gap: 10px;
    font-size: 22px;
    color: var(--magenta);
  }
  .social-square { width: 34px; height: 34px; border-radius: 6px; background: var(--magenta); }
</style>
</head>
<body>
<div class="card">
  <svg class="lens-photo" viewBox="0 0 1200 741" role="img" aria-label="Close-up photograph of a camera lens with hood, in deep navy tones">
    <defs>
      <radialGradient id="lensGlass" cx="0.42" cy="0.55" r="0.6">
        <stop offset="0" stop-color="#5a5f86"/>
        <stop offset="0.25" stop-color="var(--lens-deep)"/>
        <stop offset="0.55" stop-color="var(--lens-mid)"/>
        <stop offset="0.85" stop-color="var(--lens-rim)"/>
        <stop offset="1" stop-color="var(--lens-deep)"/>
      </radialGradient>
    </defs>
    <rect x="0" y="300" width="120" height="441" fill="var(--lens-deep)"/>
    <circle cx="275" cy="520" r="360" fill="url(#lensGlass)"/>
  </svg>

  <div class="brand">
    <span class="brand-dot"></span>
    <span class="brand-name">Danielle Whitcombe Photography</span>
  </div>

  <div class="details">
    <h1 class="name"><span class="name-first">Danielle</span> <span class="name-last">Whitcombe</span></h1>
    <p class="contact phone">0438 562 073</p>
    <p class="contact email">photos@daniellewhitcombe.com.au</p>
    <p class="contact web">www.daniellewhitcombe.com.au</p>
  </div>

  <div class="social">
    <span class="social-item"><span class="social-square"></span>Chatterbook</span>
    <span class="social-item"><span class="social-square"></span>Pipsqueak</span>
  </div>
</div>
</body>
</html>
```